Professional Financial services company want to rebrand their stationary

We need stationary design for Velmor Group, its a company with 4 member companys that include Velmor Auditing, Velmor Financial Consultancy, Velmor Debt Collection and Velmor Real Estate.

We are based in dubai so the designers need to keep in mind that we use both english and arabic so leave a space for the arabic writing.

We recently redesigned our Logo and would like to redesign our stationary to go along with it.

You will find attached the logo, please keep it looking professional and use the logo as a guide for colors when designing.

Good luck to everyone

Industry/Entity Type

Finance And Accounting

Font styles to use
Sans Serif

Colors
0292cd
33a6d7
3276b5
0355a3
ffffff
dbdbdb

Requirements
Must have
• Letterhead
• Business card
• Envelope small and A4
Nice to have
• Professional
• Space for Arabic and english

```html
<!DOCTYPE html>
<html lang="en">
<head>
<meta charset="utf-8">
<title>Velmor Group – Business Card</title>
<link href="https://fonts.googleapis.com/css2?family=Open+Sans:wght@400;600&family=Noto+Sans+Arabic:wght@400;600&display=swap" rel="stylesheet">
<style>
  :root {
    --stage: #3a3431;
    --card: #121314;
    --card-edge: #1b1c1e;
    --blue: #0292cd;
    --silver: #a9a9ab;
    --grey-text: #8a8a8c;
    --white: #ffffff;
    --rule: #dbdbdb;
  }
  * { margin: 0; padding: 0; box-sizing: border-box; }
  html, body { width: 1200px; height: 864px; overflow: hidden; }
  body {
    background: var(--stage);
    font-family: "Open Sans", Arial, sans-serif;
    position: relative;
  }
  .card {
    position: absolute;
    width: 540px;
    height: 310px;
    background: var(--card);
    border: 1px solid var(--card-edge);
    box-shadow: 0 14px 30px rgba(0,0,0,.45);
  }

  /* back side */
  .card--back { left: 60px; top: 80px; }
  .card--back .brand-name {
    position: absolute; left: 72px; top: 96px;
    font-weight: 600; font-size: 40px; color: var(--silver); letter-spacing: .5px;
    white-space: nowrap;
  }
  .card--back .site {
    position: absolute; left: 74px; top: 200px;
    font-size: 13px; letter-spacing: 5px; color: var(--grey-text);
    white-space: nowrap;
  }

  /* front side */
  .card--front { left: 600px; top: 430px; }
  .card--front .brand-name {
    position: absolute; right: 60px; top: 50px;
    font-weight: 600; font-size: 38px; color: var(--blue);
    white-space: nowrap;
  }
  .details {
    position: absolute; left: 0; right: 0; top: 136px;
    display: flex; justify-content: center; gap: 20px;
  }
  .details-en {
    width: 200px; text-align: right;
    color: var(--white); font-size: 13px; line-height: 1.45;
  }
  .details-en .person { color: var(--blue); font-size: 15px; }
  .details-en .role { font-size: 15px; font-weight: 600; margin-bottom: 4px; }
  .divider { width: 1px; background: var(--rule); opacity: .7; }
  .details-ar {
    width: 200px; direction: rtl; text-align: left;
    font-family: "Noto Sans Arabic", Arial, sans-serif;
    color: var(--white); font-size: 13px; line-height: 1.5;
  }
  .details-ar .person { color: var(--blue); font-size: 18px; font-weight: 600; }
  .details-ar .role { font-size: 15px; font-weight: 600; }
  .contacts {
    position: absolute; left: 50px; right: 30px; bottom: 28px;
    color: var(--white); font-size: 12.5px; line-height: 1.75;
    white-space: nowrap;
  }
  .contacts .line--second { padding-left: 14px; }
  .contacts .label { color: var(--blue); font-weight: 600; }
  .contacts .item + .item { margin-left: 10px; }
</style>
</head>
<body>
  <section class="card card--back" aria-label="Business card, back">
    <div class="brand-name">VELMOR GROUP</div>
    <div class="site">www.velmorgroup.example</div>
  </section>

  <section class="card card--front" aria-label="Business card, front">
    <div class="brand-name">VELMOR GROUP</div>
    <div class="details">
      <div class="details-en">
        <div class="person">Idris Calloway</div>
        <div class="role">President</div>
        <div>2710 Harbor Crest Road</div>
        <div>Dunmore Bay, 40215</div>
      </div>
      <div class="divider"></div>
      <div class="details-ar" lang="ar">
        <div class="person">إدريس كالواي</div>
        <div class="role">مؤسس</div>
        <div>4128 شارع النخيل</div>
        <div>دبي، الإمارات 51836</div>
      </div>
    </div>
    <div class="contacts">
      <div class="line"><span class="item"><span class="label">P:</span> 410 5927 3318</span><span class="item"><span class="label">C:</span> 410 6634 9072</span><span class="item"><span class="label">F:</span> 410 2286 7145</span></div>
      <div class="line line--second"><span class="item"><span class="label">E:</span> idris@velmorgroup.example</span><span class="item"><span class="label">W:</span> www.velmorgroup.example</span></div>
    </div>
  </section>
</body>
</html>
```